Hulls For Trade Website makeover

Hulls For Trade is in need of a makeover. It is feeling tired and needs a fresh new look and feel as well as being user friendly.

Hulls For Trade is an industry owned marketplace website for the sale of recreational boats, marina berths, chandlery, water craft like kayaks - anything related to recreation on the water. The main focus however is boats - new and used. The site is only available to industry businesses so no private sales are available on the site.

This approach ensures that the buyers know that title is guaranteed to all boats sold and that the businesses are reputable and stand behind their products.

The current site address is www.hullsfortrade.example.au

Target Market(s)

The target market are people interested in outdoor recreation - boaters, kayakers, sailors, paddle boarders, those looking for marina berths for their boat and those looking for service providers.

It should appeal to families, males and females, sports oriented people, fishermen, and those just looking for a relaxing, outdoor, healthy lifestyle.

Requirements
Must have
• Be very user friendly, intuitive in terms of searching, be uncluttered, fresh and engaging.
• Marine recreation is about lifestyle, fun and relaxation. When people buy a boat they are buying into a desirable, healthy lifestyle.
• It must present as professional and give consumers confidence about the professionalism of the businesses selling their products on the site.
Nice to have
• Good images that portray the lifestyle in the Australian marketplace.
• Cater for the needs of sellers to be able to showcase their products to consumers.
Should not have
• Be cluttered and hard to navigate.

```html
<!DOCTYPE html>
<html lang="en">
<head>
<meta charset="utf-8">
<title>Hulls For Trade</title>
<link rel="stylesheet" href="https://fonts.googleapis.com/css2?family=Barlow:wght@500;600;700&display=swap">
<style>
  :root {
    --brand-blue: #1f5ea8;
    --accent-blue: #1e9be6;
    --nav-grey: #8c8c8c;
    --dropdown-light: #d3d6dc;
    --dropdown-dark: #3b3e44;
    --page: #f2f2f2;
    --panel: #fbfbfb;
    --state-grey: #9a9a9a;
    --wood-dark: #6d4a35;
    --wood-mid: #84604a;
    --wood-light: #9a7359;
    --sea-deep: #0b2c48;
    --sea-mid: #1a5677;
    --hull-light: #e9f0f6;
    --sail-blue: #2b4f9c;
  }
  * { box-sizing: border-box; margin: 0; padding: 0; }
  html, body { width: 1200px; height: 900px; overflow: hidden; }
  body {
    position: relative;
    background: var(--page);
    font-family: "Barlow", Arial, sans-serif;
  }

  .site-header {
    position: absolute; left: 0; top: 0; width: 1200px; height: 81px;
    background: #fff; border-top: 1px solid #1b4d7a; z-index: 3;
  }
  .logo-tab {
    position: absolute; left: 113px; top: 0; width: 195px; height: 150px; z-index: 5;
    filter: drop-shadow(0 2px 3px rgba(0,0,0,.25));
  }
  .logo-tab svg { position: absolute; inset: 0; }
  .logo-name {
    position: absolute; left: 14px; top: 38px; width: 170px;
    display: flex; align-items: center; gap: 7px;
    color: var(--brand-blue); font-weight: 700; font-size: 21px; line-height: 1;
  }
  .logo-mark { width: 14px; height: 14px; background: var(--brand-blue); flex: none; }

  .main-nav a {
    position: absolute; top: 0; height: 81px; line-height: 84px;
    font-size: 15px; font-weight: 600; color: var(--nav-grey);
    text-decoration: none; text-transform: uppercase; white-space: nowrap;
  }
  .main-nav a.is-active {
    color: var(--accent-blue); border-top: 3px solid var(--accent-blue);
    line-height: 78px; left: 470px; width: 130px; text-align: center;
  }

  .hero {
    position: absolute; left: 0; top: 81px; width: 1200px; height: 637px;
    background:
      radial-gradient(ellipse 30% 25% at 95% 10%, rgba(8,36,60,.7), transparent 70%),
      radial-gradient(ellipse 35% 30% at 50% 95%, rgba(8,36,60,.75), transparent 70%),
      linear-gradient(172deg,
        var(--sea-mid) 0%, var(--sea-deep) 20%,
        #6f8fb0 30%, var(--hull-light) 38%, #f7fafc 48%,
        var(--sail-blue) 52%, #dfe8f0 58%, #f2f6f9 66%,
        #7f9cb6 74%, var(--sea-mid) 82%, var(--sea-deep) 100%);
  }
  .hero-dots { position: absolute; left: 541px; top: 539px; display: flex; gap: 16px; }
  .hero-dots span { width: 22px; height: 22px; border-radius: 50%; border: 2px solid rgba(255,255,255,.75); }
  .hero-dots span.is-current { background: #fff; }

  .dropdown {
    position: absolute; left: 466px; top: 96px; width: 218px; z-index: 4;
    background: var(--dropdown-light);
  }
  .dropdown::before {
    content: ""; position: absolute; left: 64px; top: -7px;
    border: 7px solid transparent; border-top: 0; border-bottom-color: var(--dropdown-light);
  }
  .dropdown-item {
    display: flex; align-items: center; gap: 11px; height: 46px; padding-left: 7px;
    font-size: 12px; font-weight: 600; color: #6a6a6a; text-transform: uppercase;
  }
  .dropdown-item.is-hover { background: var(--dropdown-dark); color: #e8e8e8; height: 50px; }
  .dropdown-item:last-child { height: 45px; }
  .dropdown-icon { width: 30px; height: 30px; background: #2e3035; display: grid; place-items: center; }
  .is-hover .dropdown-icon { background: var(--accent-blue); }

  .search-panel {
    position: absolute; left: 112px; top: 691px; width: 960px; height: 240px;
    background: var(--panel); box-shadow: 0 0 6px rgba(0,0,0,.2);
  }
  .search-bar {
    height: 73px; position: relative;
    background:
      repeating-linear-gradient(90deg, transparent 0 168px, rgba(60,38,24,.35) 168px 170px, transparent 170px 330px),
      repeating-linear-gradient(0deg, rgba(255,255,255,.04) 0 3px, rgba(0,0,0,.05) 3px 6px),
      linear-gradient(180deg, var(--wood-light), var(--wood-mid) 60%, var(--wood-dark));
    border-radius: 3px 3px 0 0;
    box-shadow: 0 2px 4px rgba(0,0,0,.3);
  }
  .search-title {
    position: absolute; left: 0; right: 0; top: 21px; text-align: center;
    font-size: 25px; font-weight: 700; color: #f1e9e2; letter-spacing: .3px;
    text-shadow: 0 1px 2px rgba(0,0,0,.5);
  }
  .social-links { position: absolute; left: 756px; top: 19px; display: flex; gap: 4px; }
  .social-links span {
    width: 32px; height: 32px; border-radius: 50%;
    background: radial-gradient(circle at 50% 40%, #8a6650, #5e3f2d);
    border: 1px solid rgba(40,25,15,.6);
    box-shadow: inset 0 0 0 5px rgba(255,255,255,.06), inset 0 1px 2px rgba(0,0,0,.4), 0 1px 0 rgba(255,255,255,.15);
  }
  .social-links span.is-current {
    background: radial-gradient(circle at 50% 40%, #ece7e2, #c9c0b8);
    border: 2px solid #f3efe9;
    box-shadow: inset 0 0 0 5px rgba(0,0,0,.05), 0 1px 3px rgba(0,0,0,.4);
  }

  .select-label {
    position: absolute; left: 95px; top: 139px;
    font-size: 31px; font-weight: 600; color: #cfcfcf;
    text-shadow: 0 1px 1px rgba(0,0,0,.25);
  }
  .state-list { position: absolute; left: 321px; top: 140px; display: flex; gap: 8px; }
  .state {
    position: relative; width: 40px; height: 40px;
    display: grid; place-items: center;
    background: var(--state-grey); color: #fff; font-size: 17px; font-weight: 600;
  }
  .state.is-selected {
    background: #2b2b2b; border: 2px solid var(--accent-blue);
    width: 44px; height: 44px; margin: -2px -2px 0;
  }
  .state.is-selected svg { position: absolute; left: 3px; top: 2px; }

  .search-button {
    position: absolute; left: 711px; top: 140px; width: 160px; height: 40px;
    display: flex; align-items: center; justify-content: center; gap: 10px;
    background: linear-gradient(180deg, #4cb6f3, var(--accent-blue));
    border-radius: 3px; box-shadow: 0 2px 3px rgba(0,0,0,.25);
    color: #fff; font-size: 17px; font-weight: 600;
  }
  .advanced-link {
    position: absolute; left: 0; right: 0; top: 196px; text-align: center;
    font-size: 24px; font-weight: 600; color: #c9c9c9;
  }
</style>
</head>
<body>
  <header class="site-header">
    <nav class="main-nav">
      <a href="#" style="left:406px">Home</a>
      <a href="#" class="is-active">Boats for Sale</a>
      <a href="#" style="left:631px">Brokers &amp; Dealers</a>
      <a href="#" style="left:804px">Members</a>
      <a href="#" style="left:905px">About Us</a>
      <a href="#" style="left:1008px">Contact</a>
    </nav>
  </header>

  <div class="logo-tab">
    <svg width="195" height="150" viewBox="0 0 195 150"><path d="M0 0H195V150L97 122L0 150Z" fill="#fff"/></svg>
    <div class="logo-name"><span class="logo-mark"></span>Hulls For Trade</div>
  </div>

  <section class="hero" role="img" aria-label="Aerial photo of a white sailing yacht with a blue sail cover and people on deck on deep blue water">
    <div class="hero-dots"><span class="is-current"></span><span></span><span></span></div>
  </section>

  <div class="dropdown">
    <div class="dropdown-item">
      <span class="dropdown-icon"><svg width="20" height="20" viewBox="0 0 20 20"><path d="M10 1l2.6 6 6.4.5-4.9 4.2 1.5 6.3L10 14.6 4.4 18l1.5-6.3L1 7.5 7.4 7z" fill="#fff"/></svg></span>
      New Boats
    </div>
    <div class="dropdown-item is-hover">
      <span class="dropdown-icon"><svg width="22" height="22" viewBox="0 0 22 22"><path d="M4 18L13 9M9 18L18 4" stroke="#fff" stroke-width="3" stroke-linecap="round"/></svg></span>
      Marine Accessories
    </div>
    <div class="dropdown-item">
      <span class="dropdown-icon"><svg width="22" height="22" viewBox="0 0 22 22"><circle cx="11" cy="11" r="7" fill="none" stroke="#fff" stroke-width="4" stroke-dasharray="3 2.5"/><circle cx="11" cy="11" r="4.5" fill="none" stroke="#fff" stroke-width="3"/></svg></span>
      Maring Products
    </div>
  </div>

  <section class="search-panel">
    <div class="search-bar">
      <h2 class="search-title">FIND A NEW OR USED BOATS</h2>
      <div class="social-links"><span></span><span class="is-current"></span><span></span><span></span><span></span></div>
    </div>
    <div class="select-label">Select States</div>
    <div class="state-list">
      <span class="state">QLD</span>
      <span class="state">NSW</span>
      <span class="state">VIC</span>
      <span class="state is-selected"><svg width="12" height="10" viewBox="0 0 12 10"><path d="M1 5l3 3 7-7" stroke="#1e9be6" stroke-width="2" fill="none"/></svg>TAS</span>
      <span class="state">SA</span>
      <span class="state">NT</span>
      <span class="state is-selected"><svg width="12" height="10" viewBox="0 0 12 10"><path d="M1 5l3 3 7-7" stroke="#1e9be6" stroke-width="2" fill="none"/></svg>WA</span>
    </div>
    <div class="search-button">SEARCH
      <svg width="24" height="24" viewBox="0 0 24 24"><circle cx="10" cy="10" r="7" fill="none" stroke="#fff" stroke-width="2.5"/><path d="M15 15l7 7" stroke="#fff" stroke-width="3" stroke-linecap="round"/></svg>
    </div>
    <div class="advanced-link">Advanced Search</div>
  </section>
</body>
</html>
```